B2B telecom company need web design

We need a web design for our corporate web site. The company exists since almost 10 years.
This is a DESIGN contest, you're expected to provide design only, NOT the whole website. The winner will have to provide the HTML template (with Lorem Ipsum content) and the CSS files of his design.
Our initial product is SMS peering in P2P (you send a SMS to a friend in a foreign country, great chance that your operator route your SMS to us that we route to the recipient). We're launching a bulk SMS service (marketing and application to SMS).
Target is mostly corporate, usually big corporate (operators, contents providers...) where use of SMS is part of the main business.
The web site is composed of 1 landing page and 7 content pages (plan is given for your information, all content page are using the same template and the same design, you do NOT need to make one design per page) :
* About US
Company Profile
They trust us
The Volnor Team
Partners
Contact us
* Solution
P2P SMS
A2P SMS
You only need to submit the landing page and a template page for the content (with h1, h2, h3 and h4).
Design must be based on our new logo (see attached file).
Our current web site http://www.volnor-example.com
The winner of the contest will have to provide state of the art HTML template and CSS files of his design. Photo used shall be downloaded from Pixelbrook (provide the ID of the picture that we purchase file).
Target Market(s)
Telecom operator. SMS Peering hubs. Bulk SMS.
Industry/Entity Type
It Company
Number of Pages Required
2 page

```html
<!DOCTYPE html>
<html lang="en">
<head>
<meta charset="utf-8">
<title>Volnor Mobile</title>
<link href="https://fonts.googleapis.com/css2?family=Open+Sans:wght@300;400;600;700;800&display=swap" rel="stylesheet">
<style>
:root{
  --ink:#ffffff;
  --lime:#8dbb1c;
  --hero-dark:#1f2533;
  --menu-bg:rgba(110,90,80,.72);
  --menu-line:rgba(255,255,255,.14);
  --footer-bg:rgba(22,24,32,.88);
  --muted:#d9dbe0;
}
*{margin:0;padding:0;box-sizing:border-box}
html,body{width:1200px;height:711px;overflow:hidden}
body{font-family:"Open Sans",Arial,sans-serif;color:var(--ink);background:var(--hero-dark)}
.page{position:relative;width:1200px;height:711px;overflow:hidden}
.hero-photo{position:absolute;inset:0;
  background:
    radial-gradient(ellipse 320px 360px at 880px 330px,rgba(160,110,80,.55),transparent 70%),
    radial-gradient(ellipse 200px 260px at 500px 330px,rgba(70,78,92,.7),transparent 70%),
    linear-gradient(180deg,#3b4454 0%,#2c3342 45%,#1d2230 100%);}
.logo{position:absolute;left:100px;top:58px;font-size:28px;font-weight:400;letter-spacing:1px;color:var(--ink);display:flex;align-items:center;gap:10px}
.logo-mark{width:10px;height:10px;background:var(--lime)}
.main-nav{position:absolute;top:68px;left:495px;display:flex;font-size:13px;letter-spacing:1px}
.main-nav a{color:var(--ink);text-decoration:none;position:absolute;white-space:nowrap}
.nav-home{left:0}.nav-news{left:110px}.nav-about{left:217px}.nav-services{left:332px}.nav-contact{left:463px}
.nav-services svg{margin-left:6px;vertical-align:middle}
.menu-toggle{position:absolute;left:1080px;top:64px;width:21px;height:20px;display:flex;flex-direction:column;justify-content:space-between}
.menu-toggle span{height:3px;background:var(--ink)}
.submenu{position:absolute;left:826px;top:98px;width:144px;background:var(--menu-bg);list-style:none}
.submenu li{height:27.4px;line-height:27.4px;padding-left:14px;font-size:7.5px;letter-spacing:.8px;border-bottom:1px solid var(--menu-line)}
.submenu li:last-child{border-bottom:none}
.slide-dots{position:absolute;left:1092px;top:229px;list-style:none}
.slide-dots li{width:8px;height:8px;border-radius:50%;background:var(--ink);margin-bottom:17px}
.slide-dots li.active{background:transparent;border:1.5px solid var(--ink);opacity:.8}
.hero-title{position:absolute;top:255px;left:0;width:1200px;text-align:center;font-size:62px;font-weight:800;letter-spacing:1px}
.hero-sub{position:absolute;top:341px;left:0;width:1200px;text-align:center;font-size:34px;font-weight:300;letter-spacing:3.6px;white-space:nowrap}
.services{position:absolute;top:532px;left:0;width:1200px}
.service{position:absolute;width:290px}
.service:nth-child(1){left:100px}.service:nth-child(2){left:460px}.service:nth-child(3){left:837px}
.service h3{color:var(--lime);font-size:13px;font-weight:600;margin-bottom:6px}
.service p{font-size:11.5px;line-height:21.5px;color:var(--ink)}
.service p svg{vertical-align:-2px;margin-left:4px}
.divider{position:absolute;top:527px;height:94px;border-left:1px dotted rgba(255,255,255,.45)}
.divider.one{left:412px}.divider.two{left:778px}
.site-footer{position:absolute;left:0;top:663px;width:1200px;height:48px;background:var(--footer-bg);font-size:9.5px;letter-spacing:1.3px;color:var(--muted)}
.legal{position:absolute;left:101px;top:18px;white-space:nowrap}
.legal span{margin:0 12px}
.follow{position:absolute;left:861px;top:18px;display:flex;align-items:center;gap:20px}
.follow i{display:block;width:10px;height:10px;border-radius:50%;background:var(--muted)}
.follow b{font-weight:400;margin-right:-6px}
</style>
</head>
<body>
<div class="page">
  <div class="hero-photo" role="img" aria-label="Blurred photograph of a young woman photographing herself with a smartphone"></div>

  <div class="logo"><span>VOLNOR mobile</span><span class="logo-mark"></span></div>

  <nav class="main-nav">
    <a class="nav-home" href="#">HOME</a>
    <a class="nav-news" href="#">NEWS</a>
    <a class="nav-about" href="#">ABOUT</a>
    <a class="nav-services" href="#">SERVICES<svg width="8" height="6" viewBox="0 0 8 6"><path d="M1 1l3 3 3-3" fill="none" stroke="#fff" stroke-width="1.4"/></svg></a>
    <a class="nav-contact" href="#">CONTACT US</a>
  </nav>
  <div class="menu-toggle"><span></span><span></span><span></span></div>

  <ul class="submenu">
    <li>MOBILE EXCHANGE</li>
    <li>MOBILE ADVANTAGE</li>
    <li>MOBILE INTEROPERABILITY</li>
    <li>MOBILE SOLUTIONS</li>
    <li>TECHNOLOGY</li>
  </ul>

  <ul class="slide-dots">
    <li class="active"></li><li></li><li></li><li></li><li></li>
  </ul>

  <h1 class="hero-title">VOLNOR</h1>
  <p class="hero-sub">GLOBAL &amp; REGIONAL SMS EXCHANGE</p>

  <section class="services">
    <article class="service">
      <h3>OPERATOR SERVICES</h3>
      <p>Volnor Mobile Exchange offers operators comprehensive services to facilitate the delivery of mobile data and content.<svg width="10" height="10" viewBox="0 0 10 10"><circle cx="5" cy="5" r="5" fill="#8dbb1c"/><path d="M4 2.8l2.2 2.2L4 7.2" fill="none" stroke="#1f2533" stroke-width="1.4"/></svg></p>
    </article>
    <article class="service">
      <h3>BRAND &amp; CONTENT SERVICES</h3>
      <p>Volnor Mobile Exchange offers operators comprehensive services to facilitate the delivery of mobile data and content.<svg width="10" height="10" viewBox="0 0 10 10"><circle cx="5" cy="5" r="5" fill="#8dbb1c"/><path d="M4 2.8l2.2 2.2L4 7.2" fill="none" stroke="#1f2533" stroke-width="1.4"/></svg></p>
    </article>
    <article class="service">
      <h3>ENTERPRISE SERVICES</h3>
      <p>Volnor Mobile Exchange offers operators comprehensive services to facilitate the delivery of mobile data and content.<svg width="10" height="10" viewBox="0 0 10 10"><circle cx="5" cy="5" r="5" fill="#8dbb1c"/><path d="M4 2.8l2.2 2.2L4 7.2" fill="none" stroke="#1f2533" stroke-width="1.4"/></svg></p>
    </article>
  </section>
  <div class="divider one"></div>
  <div class="divider two"></div>

  <footer class="site-footer">
    <div class="legal">© 2015. VOLNOR. ALL RIGHTS RESERVED.<span>/</span>TERMS &amp; CONDITIONS<span>/</span>PRIVACY POLICY</div>
    <div class="follow"><b>FOLLOW US :</b><i></i><i></i><i></i><i></i><i></i></div>
  </footer>
</div>
</body>
</html>
```